Flyer-Design für Hilfe zur Digitalisierung von Unternehmen
Vielen Dank für den schnellen Entwurf & die kurzfristigen Änderungen! Top!
Zielgruppe
Marketing
Schwerpunkte: Websites, Webshops, Travik Ads, Social Ads
Zielgruppe: kleine & mittelständische Unternehmen
Aufgabenstellung
Text bitte nur Inhaltlich übernehmen, bin nicht der große Poet! ;-)
Digitalisierung des Unternehmens / Im Zuge der aktuellen Lage # Corona , ist die Digitalisierung wieder ein Stück weiter ins Zentrum unseres Leben gerückt / Wir wollen Ihnen helfen auch Ihr Geschäft zu Digitalisieren, / In diesem Zuge haben wir ein einmaliges Angebot für Sie gestrickt. Ein voll funktionsfähigen Online Shop inkl. der ersten 5 Artikel ab 1999,00 €
weitere Angebote:
Webshops inkl. 5 Artikeln 1999,00
Website 5 Seiten 799,00
Travik Ads ab 60,00 mtl. keine Setup Gebühr
Social Ads ab 60,00 mtl. keine Setup Gebühr
für mehr Information können Sie uns gerne Kontaktieren / bzw ein persönlichen Termin vor Ort vereinbaren

```html
<!DOCTYPE html>
<html lang="de">
<head>
<meta charset="utf-8">
<title>Nordlicht Medien GmbH – Flyer</title>
<link rel="stylesheet" href="https://fonts.googleapis.com/css2?family=Source+Sans+3:wght@300;400;600;700&display=swap">
<style>
  :root {
    --navy-deep: #0c2a45;
    --navy-panel: #1b5472;
    --sky: #21a7e0;
    --glass: rgba(125, 205, 230, 0.55);
    --photo-a: #173a5e;
    --photo-b: #2c7fb8;
    --photo-c: #5cb8d8;
    --white: #ffffff;
  }
  html, body {
    margin: 0;
    padding: 0;
    width: 851px;
    height: 1200px;
    overflow: hidden;
    background: var(--white);
  }
  .flyer {
    position: relative;
    width: 851px;
    height: 1200px;
    overflow: hidden;
    font-family: "Source Sans 3", "Myriad Pro", sans-serif;
    color: var(--white);
  }
  .backdrop {
    position: absolute;
    inset: 0;
    background:
      linear-gradient(180deg, rgba(6, 20, 36, 0) 55%, rgba(6, 20, 36, 0.85) 100%),
      linear-gradient(110deg, var(--photo-a) 0%, var(--photo-b) 45%, var(--photo-c) 80%, #3f8fb5 100%);
  }
  .shapes {
    position: absolute;
    inset: 0;
    width: 851px;
    height: 1200px;
  }
  .shape-offer { fill: var(--navy-panel); }
  .shape-glass { fill: var(--glass); }
  .shape-social { fill: var(--sky); }

  .brand {
    position: absolute;
    left: 41px;
    top: 60px;
    display: flex;
    align-items: center;
    gap: 12px;
  }
  .brand-mark {
    width: 34px;
    height: 34px;
    background: var(--white);
  }
  .brand-name {
    font-weight: 600;
    font-size: 30px;
    line-height: 1.05;
    letter-spacing: 0.5px;
  }

  .centered {
    position: absolute;
    transform: translate(-50%, -50%);
    white-space: nowrap;
    text-align: center;
    margin: 0;
    line-height: 1;
  }
  .headline { font-weight: 600; font-size: 31px; }
  .price-big { font-weight: 700; font-size: 78px; letter-spacing: -1px; }
  .service-title { font-weight: 600; font-size: 35px; }
  .service-price { font-weight: 700; font-size: 70px; letter-spacing: -1px; }
  .service-price .unit { font-size: 42px; margin-left: 6px; }
  .service-note { font-weight: 600; font-size: 35px; }
  .network-name { font-weight: 600; font-size: 30px; }

  .growth-icon {
    position: absolute;
    left: 600px;
    top: 292px;
    width: 120px;
    height: 90px;
  }

  .cta { font-weight: 400; font-size: 48px; }
  .contact-line { font-weight: 400; font-size: 30px; }
</style>
</head>
<body>
<main class="flyer">
  <div class="backdrop" role="img" aria-label="Unscharfes Hintergrundfoto: Geschäftsmann im Anzug vor einer Stadtkulisse in Blautönen"></div>

  <svg class="shapes" viewBox="0 0 1240 1748" preserveAspectRatio="none" aria-hidden="true">
    <polygon class="shape-offer" points="495,365 705,0 1240,0 1240,290 1020,665"/>
    <polygon class="shape-glass" points="175,935 470,400 1000,700 705,1230"/>
    <polygon class="shape-social" points="0,1245 155,970 690,1255 430,1748 0,1748"/>
  </svg>

  <div class="brand">
    <span class="brand-mark"></span>
    <span class="brand-name">NORDLICHT<br>MEDIEN GMBH</span>
  </div>

  <p class="centered headline" style="left:622px; top:107px;">Ihre Online-Präsenz</p>
  <p class="centered headline" style="left:622px; top:148px;">Website 5 Seiten</p>
  <p class="centered price-big" style="left:622px; top:234px;">799,00</p>

  <svg class="growth-icon" viewBox="0 0 120 90" aria-hidden="true">
    <polyline points="3,0 3,87 120,87" fill="none" stroke="#fff" stroke-width="5"/>
    <polyline points="18,66 45,40 62,56 100,18" fill="none" stroke="#fff" stroke-width="9" stroke-linejoin="miter"/>
    <polygon points="80,10 111,7 108,38" fill="#fff"/>
  </svg>

  <p class="centered service-title" style="left:401px; top:477px;">Travik Ads</p>
  <p class="centered service-price" style="left:401px; top:562px;">ab 60,00<span class="unit">mtl.</span></p>
  <p class="centered service-note" style="left:401px; top:621px;">keine Setup Gebühr</p>
  <p class="centered network-name" style="left:452px; top:729px;">Travik</p>

  <p class="centered service-title" style="left:211px; top:820px;">Social Ads</p>
  <p class="centered service-price" style="left:205px; top:906px;">ab 60,00<span class="unit">mtl.</span></p>
  <p class="centered service-note" style="left:211px; top:966px;">keine Setup Gebühr</p>
  <p class="centered network-name" style="left:219px; top:1084px;">Frendo</p>

  <p class="centered cta" style="left:676px; top:773px;">Mehr Infos</p>
  <p class="centered cta" style="left:676px; top:835px;">hier:</p>

  <p class="centered contact-line" style="left:636px; top:907px;">+49 (0) 2 11 40 55 12 90</p>
  <p class="centered contact-line" style="left:636px; top:948px;">info@platzimweb-demo.de</p>
  <p class="centered contact-line" style="left:636px; top:989px;">www.platzimweb-demo.de</p>

  <p class="centered contact-line" style="left:636px; top:1071px;">NORDLICHT MEDIEN GMBH</p>
  <p class="centered contact-line" style="left:636px; top:1112px;">Am Lindenhof 14</p>
  <p class="centered contact-line" style="left:636px; top:1153px;">46100 Musterstadt</p>
</main>
</body>
</html>
```